Touring Cabaret Seasons Needs a Poster Design

We need a poster design for upcoming Cabaret seasons in Melbourne and Adelaide (Australia) for a prestigious festival.

Show is titled "Here's a Small Thing I Dreamed Up Last Week..." and is a comedy parody of bad cabaret and deluded performers. We'd like the poster to reflect the comedy of the piece without being silly and inaccessable.

Artist has recently won awards for this show and these will need to be listed as a part of the design.

I have attached a couple of photographs that can be used - one is the artist with a blank book cover and these could be used to overlay text.

Would like it to not look too wordy, however I realise we've asked for a lot of text to be included.

Target Market(s)

Ages 20 - 40 cabaret or comedy fans.

Industry/Entity Type

Festival

Requirements
Must have
• TEXT:
The Velvet Parlour presents:
Here's a Small Thing I Dreamed Up Last Week...

TEXT:
WINNER of BEST CABARET, BEST WRITING and PEOPLE’S CHOICE awards at Quick + Tidy Revue 2011

TEXT:
The Lantern Room (Melbourne)
Feb 23rd to the 26th

Le Corbeau, REVedge(Adelaide)
March 3rd and 4th

QUOTES:
“...the funniest things in spandex. 4.5 stars” – The Courier Post on Rally! A revue about lawn bowls.

“a clever dissection of bad cabaret” – Owen Blackwood, The Courier Post on Quick + Tidy Revue
Nice to have
• TEXT:
The last time someone showed you a little something they were working on, did you lose an hour of your life you will never get back? Don’t worry – we’ve all been there.

TEXT:
Composer and co-writer of Rally! (A revue about lawn bowls) and WINNER of BEST CABARET, BEST WRITING and PEOPLE’S CHOICE awards at Quick + Tidy Revue 2011, presents her full show, with more original music and helpful anecdotes.

WEBSITE:
More info at www.mingleface.example/thevelvetparlour

```html
<!DOCTYPE html>
<html lang="en">
<head>
<meta charset="utf-8">
<title>Here's a Small Thing I Dreamed Up Last Week... — The Velvet Parlour</title>
<link rel="stylesheet" href="https://fonts.googleapis.com/css2?family=Arvo:wght@700&family=Josefin+Sans:wght@400;600&family=Oswald:wght@400;500;600&display=swap">
<style>
  :root {
    --paper-light: #eeeedd;
    --paper-mid: #d9dcc4;
    --hair-warm: #8a5a3c;
    --skin-warm: #d9b79a;
    --edge-dark: #1e2326;
    --ink: #2e3d48;
    --ink-soft: #3b4a54;
    --title-glow: #f4f1d8;
    --ribbon: #1f2f45;
    --ribbon-text: #f2f2ea;
  }
  * { margin: 0; padding: 0; box-sizing: border-box; }
  html, body { width: 848px; height: 1200px; overflow: hidden; background: var(--paper-light); }
  .poster {
    position: relative;
    width: 848px;
    height: 1200px;
    overflow: hidden;
    font-family: "Josefin Sans", sans-serif;
    color: var(--ink);
  }
  .poster__backdrop {
    position: absolute;
    inset: 0;
    background:
      radial-gradient(ellipse 30% 22% at 100% 0%, rgba(70,95,95,0.4), rgba(70,95,95,0)),
      radial-gradient(ellipse 26% 18% at 0% 0%, rgba(70,95,95,0.25), rgba(70,95,95,0)),
      linear-gradient(180deg, #e3e7d6 0%, var(--paper-mid) 50%, #cfd0b8 100%);
  }
  .poster__photo {
    position: absolute;
    left: 84px;
    top: 130px;
    width: 680px;
    height: 1070px;
    border-radius: 260px 260px 0 0;
    background:
      linear-gradient(180deg,
        rgba(138,90,60,0.55) 0%,
        rgba(150,100,70,0.5) 16%,
        rgba(217,183,154,0.55) 26%,
        rgba(217,183,154,0.5) 36%,
        rgba(236,234,214,0.95) 39%,
        rgba(236,234,214,0.95) 88%,
        rgba(200,190,170,0.9) 100%);
    box-shadow: 0 0 40px 20px rgba(217,220,196,0.9) inset;
  }
  .poster__photo::before,
  .poster__photo::after {
    content: "";
    position: absolute;
    top: 530px;
    width: 120px;
    height: 540px;
    background: linear-gradient(180deg, rgba(30,35,38,0.85), rgba(30,35,38,0.95));
  }
  .poster__photo::before { left: -84px; border-radius: 0 40px 0 0; }
  .poster__photo::after { right: -84px; border-radius: 40px 0 0 0; }

  .award {
    position: absolute;
    left: 58px;
    top: 146px;
    width: 180px;
    text-align: center;
    color: var(--ink);
    text-transform: uppercase;
  }
  .award__title { font-weight: 400; font-size: 25px; letter-spacing: 1px; line-height: 1; }
  .award__detail { font-weight: 600; font-size: 12.5px; line-height: 1.25; margin-top: 4px; }
  .award__year { font-weight: 400; font-size: 24px; line-height: 1; margin-top: 4px; }

  .reviews {
    position: absolute;
    right: 44px;
    top: 84px;
    width: 460px;
    text-align: right;
    text-transform: uppercase;
    color: var(--ink-soft);
  }
  .review + .review { margin-top: 8px; }
  .review__quote { font-size: 13.5px; letter-spacing: 0.8px; line-height: 1.3; }
  .review__source { font-weight: 600; font-size: 12px; letter-spacing: 0.6px; line-height: 1.3; }

  .show {
    position: absolute;
    left: 0;
    right: 0;
    top: 606px;
    text-align: center;
  }
  .show__presenter {
    font-size: 19px;
    letter-spacing: 2.6px;
    text-transform: uppercase;
    color: var(--ink-soft);
  }
  .show__title {
    margin-top: 24px;
    font-family: "Arvo", serif;
    font-weight: 700;
    font-size: 56px;
    line-height: 72px;
    color: var(--ink);
    text-shadow: 0 0 3px var(--title-glow), 0 0 6px var(--title-glow), 0 0 10px var(--title-glow);
  }

  .dates {
    position: absolute;
    left: 0;
    right: 0;
    top: 838px;
    text-align: center;
    font-family: "Oswald", sans-serif;
    text-transform: uppercase;
    color: var(--ink);
  }
  .dates__venue { font-weight: 500; font-size: 20px; line-height: 28px; }
  .dates__when { font-weight: 500; font-size: 32px; line-height: 42px; letter-spacing: 0.5px; }
  .dates__venue--second { margin-top: 24px; }

  .more-info {
    position: absolute;
    left: 152px;
    top: 1100px;
    width: 556px;
    height: 52px;
  }
  .more-info svg { position: absolute; inset: 0; }
  .more-info__text {
    position: relative;
    line-height: 52px;
    padding-left: 22px;
    font-family: "Oswald", sans-serif;
    font-weight: 500;
    font-size: 17px;
    letter-spacing: 0.6px;
    text-transform: uppercase;
    color: var(--ribbon-text);
  }
</style>
</head>
<body>
<main class="poster">
  <div class="poster__backdrop"></div>
  <div class="poster__photo" role="img" aria-label="Photograph of the performer peering over a blank book cover held up to her face, in muted pale green and cream tones"></div>

  <section class="award">
    <p class="award__title">Winner</p>
    <p class="award__detail">Best Cabaret,<br>Best Writing<br>and People's Choice<br>at Quick + Tidy<br>Revue</p>
    <p class="award__year">2011</p>
  </section>

  <section class="reviews">
    <div class="review">
      <p class="review__quote">“A clever dissection of bad cabaret”</p>
      <p class="review__source">– Owen Blackwood, The Courier Post on Quick + Tidy Revue</p>
    </div>
    <div class="review">
      <p class="review__quote">“...the funniest things in spandex. 4.5 stars”</p>
      <p class="review__source">– The Courier Post on Rally! A revue about lawn bowls</p>
    </div>
  </section>

  <header class="show">
    <p class="show__presenter">The Velvet Parlour presents</p>
    <h1 class="show__title">Here's a Small Thing I<br>Dreamed Up Last Week...</h1>
  </header>

  <section class="dates">
    <p class="dates__venue">The Lantern Room (Melbourne)</p>
    <p class="dates__when">Feb 23rd to the 26th</p>
    <p class="dates__venue dates__venue--second">Le Corbeau, REVedge (Adelaide)</p>
    <p class="dates__when">March 3rd and 4th</p>
  </section>

  <footer class="more-info">
    <svg width="556" height="52" viewBox="0 0 556 52" aria-hidden="true">
      <polygon points="0,4 532,4 556,48 0,48" fill="var(--ribbon)"/>
    </svg>
    <p class="more-info__text">More info @ www.mingleface.example/thevelvetparlour</p>
  </footer>
</main>
</body>
</html>
```